Bright and vibrant Jewelry Designer Web Page

Hi creative artists,

My name is Marta, I'm a local jewelry designer with a small store in Duesseldorf Germany. All my Jewelrys are unique and hand crafted by my self.

My designs are colorful, young, modern and trendy as well as timeless and durable due to the high quality materials. I use gold, silver, jewelry, fresh water pearls and hand crafted glass.

Competitors are local goldsmith which produce custom-made jewelry.

I have started my business with my jewelry label "twigs and ribbons" 2007:
http://www.twigs-and-ribbons.de/start.php

In 2009 I have opened my store "Kupfer und Leinen" (silver and silk) together with a fashion designer:
http://www.kupfer-leinen.de/home.php
https://www.facebook.com/Kupfer.und.Leinen (latest jewelrys)

Scope of pages:
● welcome page
● category overview
- short introduction
- sub categories: Earring, Necklace, Ring, Bride Jewelry, ...
● category page
- short introduction
- products of this category
● product page
- short introduction
- about 3 to 4 pictures
- description: materials, dimensions
- price
- ! important ! related products
● contact page
- address
- contact form
● blog
- picture
- text

Conclusion:
● We need a emotional page
● Lots of impressive and brilliant product images
● A feminine touch
● Last but not least the design should reflect
- outstanding design
- uniqueness
- made-to-measure

Target Market(s)

Women in the mid 20's and 30's , interested in individual style, fashion and luxury goods

Industry/Entity Type

Jewelry

Requirements
Must have
• ● css for screen, mobile devices and print
● full function also with out JavaScript
● only use free available fonts e.g. Lumora Type Library (http://www.lumoratype.example/webfonts)
Should not have
• ● sound
● flash

```html
<!DOCTYPE html>
<html lang="en">
<head>
<meta charset="utf-8">
<title>Topaz Necklace – Kupfer und Leinen</title>
<link rel="stylesheet" href="https://fonts.googleapis.com/css2?family=Gelasio:ital,wght@0,400;0,600;0,700;1,400;1,600&family=Open+Sans:wght@400;600&display=swap">
<style>
:root{
  --pink:#e5adbb;
  --pink-mid:#dd8fa3;
  --pink-deep:#c55677;
  --rose-text:#b9496b;
  --band-light:#f3cbd5;
  --cream:#f7f4ec;
  --ink:#3d3d3d;
  --ink-soft:#666;
  --rule:#e6e1da;
  --white:#fff;
  --serif:"Gelasio",Georgia,serif;
  --sans:"Open Sans",Arial,sans-serif;
}
*{box-sizing:border-box;margin:0;padding:0}
html,body{width:938px;height:1200px;overflow:hidden;background:var(--white)}
body{position:relative;font-family:var(--sans);color:var(--ink)}
.abs{position:absolute}
a{color:inherit;text-decoration:none}
ul{list-style:none}
h1,h2,h3{font-weight:400}

.top-rule{left:0;top:0;width:938px;height:5px;background:var(--pink)}
.bottom-rule{left:0;top:1194px;width:938px;height:6px;background:var(--pink)}

.brand{left:140px;top:30px;display:flex;align-items:center;gap:8px}
.brand-mark{width:18px;height:18px;border-radius:50%;background:var(--pink-mid)}
.brand-name{font-family:var(--serif);font-size:25px;color:#8a8a8a;font-weight:400;letter-spacing:-.3px}

.social{top:40px;width:9px;height:9px;border-radius:50%;background:var(--band-light)}
.search{left:706px;top:35px;width:86px;height:17px;border:1px solid #e3e3e3;border-radius:3px;
  font-family:var(--serif);font-style:italic;font-size:8px;color:#aaa;padding:3px 8px}
.search svg{position:absolute;right:5px;top:4px}

.main-nav{left:562px;top:77px;display:flex;font-family:var(--serif);font-size:11.5px;color:var(--ink)}
.main-nav li{margin-right:16px}
.main-nav li.active{position:relative}
.main-nav li.active::before{content:"";position:absolute;left:-7px;top:-10px;width:42px;height:33px;
  border-left:1px solid #e8e8e8;border-right:1px solid #e8e8e8;border-top:1px solid #eee}
.main-nav li:last-child{margin-right:0}

.dropdown{left:607px;top:100px;width:126px;height:148px;background:var(--cream);
  box-shadow:0 2px 4px rgba(0,0,0,.18);z-index:5;padding:12px 0 0 24px;font-family:var(--serif);font-size:9.5px}
.dropdown li{height:27px;color:var(--ink)}
.dropdown li.current{color:var(--pink-deep)}

.title-band{left:0;top:110px;width:938px;height:66px;
  background:linear-gradient(90deg,#f1c3ce 0%,#e9a8b8 30%,#eab0be 60%,#f4d0d8 100%);
  border-top:2px dotted #fff;border-bottom:2px dotted #fff}
.page-title{left:147px;top:125px;font-family:var(--serif);font-size:21px;color:var(--white)}
.page-sub{left:147px;top:150px;font-family:var(--serif);font-size:12px;color:var(--pink-deep)}

.breadcrumb{left:147px;top:199px;font-family:var(--serif);font-size:9.5px;color:var(--ink)}
.breadcrumb em{font-style:italic}
.rule-h{height:1px;background:var(--rule)}

.product-photo{left:148px;top:262px;width:175px;height:171px;
  background:linear-gradient(135deg,#dfe7e6 0%,#9fd3de 30%,#eef2f1 50%,#c9dadd 70%,#e9ede9 100%)}
.gallery-arrow{top:331px;width:22px;height:22px;border-radius:50%;background:var(--white);
  box-shadow:0 1px 2px rgba(0,0,0,.25);display:flex;align-items:center;justify-content:center}

.intro{left:357px;top:262px;width:214px;font-family:var(--serif);font-style:italic;font-weight:600;
  font-size:7.6px;line-height:11.8px;color:var(--ink)}
.add-cart{left:358px;top:396px;width:158px;height:35px;border-radius:4px;
  background:linear-gradient(#ec8aa3,#d9587c);box-shadow:0 1px 2px rgba(0,0,0,.25);
  display:flex;align-items:center;padding-left:12px;gap:8px;
  font-family:var(--serif);font-size:17px;color:var(--white)}

.description{left:150px;top:462px;width:424px;font-size:7.8px;line-height:12.3px;color:var(--ink)}

.sidebar{left:608px;top:248px;width:185px;height:350px;
  background:linear-gradient(90deg,#f6f6f6 0,#fff 10px)}
.sidebar-list{left:630px;top:276px;font-size:7.6px;color:var(--ink-soft)}
.sidebar-list li{height:16.8px;padding-left:9px;position:relative}
.sidebar-list li::before,.footer-list li::before{content:"";position:absolute;left:0;top:3px;
  border-left:3px solid currentColor;border-top:2px solid transparent;border-bottom:2px solid transparent}
.side-heading{left:624px;top:418px;font-family:var(--serif);font-size:11px;color:var(--ink)}
.field-label{font-size:6.5px;color:var(--ink)}
.field{border:1px solid #d8d8d8;background:var(--white)}
.send{left:708px;top:567px;font-family:var(--serif);font-style:italic;font-size:9.5px;color:var(--pink-mid)}

.related-tab{left:325px;top:633px;width:106px;height:26px;background:var(--cream);border:1px solid #e6e1d6;
  font-size:8.5px;color:#555;text-align:center;line-height:24px;letter-spacing:.2px}

.product-card{top:686px;width:80px}
.product-card .thumb{position:absolute;left:2px;top:5px;width:78px;height:71px;
  background:linear-gradient(90deg,#d9d5d3 0%,#c92a2a 40%,#b01e1e 60%,#d3cfcd 100%)}
.price-tag{position:absolute;left:0;top:0;width:32px;height:36px;background:#f0b8c5;border-radius:2px;
  font-family:var(--serif);font-size:8px;color:var(--white);text-align:center;padding-top:15px}
.price-tag::before{content:"$";position:absolute;left:11px;top:-3px;width:10px;height:10px;border-radius:50%;
  background:var(--pink-deep);font-size:6px;line-height:10px}
.product-card h3{position:absolute;left:3px;top:78px;font-family:var(--serif);font-size:9px;font-weight:600;color:var(--ink);white-space:nowrap}
.card-actions{position:absolute;left:2px;top:96px;display:flex;gap:2px;font-size:6px;font-weight:600;color:#666}
.card-actions span{background:var(--cream);height:14px;line-height:14px;padding-left:6px}
.card-actions span:first-child{width:41px}
.card-actions span:last-child{width:34px}

.footer{left:0;top:946px;width:938px;height:205px;background:var(--pink);border-top:2px dotted #fff;border-bottom:2px dotted #fff}
.footer-brand{left:142px;top:976px;display:flex;align-items:center;gap:6px}
.footer-brand .brand-name{font-size:18px;color:#9c7b83}
.footer-about{left:147px;top:1013px;width:140px;font-size:7.2px;line-height:11.4px;color:var(--white)}
.footer-heading{top:989px;font-family:var(--serif);font-size:11.5px;color:var(--rose-text)}
.footer-list{top:1014px;font-size:7.6px;color:var(--white)}
.footer-list li{height:16.8px;padding-left:10px;position:relative}

.bottom-nav{left:147px;top:1168px;display:flex;gap:7px;font-family:var(--serif);font-size:11px;color:var(--ink)}
.bottom-nav .current{color:var(--pink-mid);font-style:italic}
</style>
</head>
<body>

<div class="abs top-rule"></div>

<header>
  <a class="abs brand" href="#"><span class="brand-mark"></span><span class="brand-name">Kupfer und Leinen</span></a>
  <span class="abs social" style="left:666px"></span>
  <span class="abs social" style="left:686px"></span>
  <div class="abs search">Search...
    <svg width="7" height="7" viewBox="0 0 8 8"><circle cx="3.2" cy="3.2" r="2.4" fill="none" stroke="#999"/><line x1="5" y1="5" x2="7.5" y2="7.5" stroke="#999"/></svg>
  </div>
  <nav><ul class="abs main-nav">
    <li>Home</li><li class="active">Silver</li><li>Silk</li><li>Blog</li><li>Contact</li>
  </ul></nav>
  <ul class="abs dropdown">
    <li>Earrings</li><li class="current">Necklaces</li><li>Rings</li><li>Bridal Jewellery</li>
  </ul>
</header>

<div class="abs title-band"></div>
<h1 class="abs page-title">Topaz Necklace</h1>
<p class="abs page-sub">Handcrafted silver and topaz necklace</p>

<p class="abs breadcrumb">Home &nbsp;»&nbsp; Silver &nbsp;»&nbsp; <em>Topaz Earrings</em></p>
<div class="abs rule-h" style="left:147px;top:222px;width:645px"></div>

<main>
  <div class="abs product-photo" role="img" aria-label="Close-up photo of the silver and blue topaz necklace"></div>
  <span class="abs gallery-arrow" style="left:133px"><svg width="6" height="8" viewBox="0 0 6 8"><path d="M5 0 1 4l4 4" fill="none" stroke="#444" stroke-width="1.6"/></svg></span>
  <span class="abs gallery-arrow" style="left:316px"><svg width="6" height="8" viewBox="0 0 6 8"><path d="M1 0l4 4-4 4" fill="none" stroke="#444" stroke-width="1.6"/></svg></span>

  <p class="abs intro">Nulla facilisi. Nulla facilisi. Sed gravida sapien quis leo tempus ullamcorper interdum enim eleifend. Aliquam mi enim, malesuada sodales ultrices eget, bibendum ac libero. In sagittis rutrum lacus, nec rhoncus risus vehicula sed. Ut vel eros metus, ac feugiat tortor. Etiam elit risus, ullamcorper non blandit sit amet, varius in mi. Mauris condimentum dui eu libero iaculis pharetra.</p>

  <a class="abs add-cart" href="#">
    <svg width="22" height="14" viewBox="0 0 22 14"><path d="M1 2h4l3 9h10M8 4v5M12 4v5" fill="none" stroke="#fff" stroke-width="1.5"/></svg>
    Add To Cart
  </a>

  <p class="abs description">Nulla facilisi. Nulla facilisi. Sed gravida sapien quis leo tempus ullamcorper interdum enim eleifend. Aliquam mi enim, malesuada sodales ultrices eget, bibendum ac libero. In sagittis rutrum lacus, nec rhoncus risus vehicula sed. Ut vel eros metus, ac feugiat tortor. Etiam elit risus, ullamcorper non blandit sit amet, varius in mi. Mauris condimentum dui eu libero iaculis pharetra. Aliquam mollis nisi sit amet sapien pellentesque ullamcorper. Quisque eros ligula, iaculis in tempor ac, tristique vitae dolor. Vivamus varius, nulla adipiscing eleifend condimentum, lectus eros molestie tellus, in volutpat nibh ante at ipsum. Nunc varius felis eget eros viverra ut dapibus nunc condimentum. Praesent massa metus, congue ac consectetur et, vulputate et turpis. Nulla interdum, turpis non rhoncus luctus, augue purus iaculis justo, eget hendrerit est quam interdum lectus. Suspendisse facilisis pharetra accumsan. Suspendisse potenti. Duis augue leo, tempus at tristique ut, iaculis non diam. Maecenas scelerisque erat et nisl laoreet sollicitudin. Fusce vehicula enim nec eros hendrerit lacinia. Suspendisse a nisi orci, at luctus augue. Praesent hendrerit vestibulum ligula ultrices viverra. Pellentesque iaculis diam eros. Quisque suscipit massa pellentesque magna ornare eget laoreet velit lobortis. Mauris eros</p>

  <div class="abs rule-h" style="left:148px;top:645px;width:459px"></div>
  <h2 class="abs related-tab">RELATED PRODUCTS</h2>

  <article class="abs product-card" style="left:146px"><div class="thumb" role="img" aria-label="Product photo of a red silk dress"></div><span class="price-tag">105</span><h3>Red Silk Dress</h3><div class="card-actions"><span>⊻ CART</span><span>? INFO</span></div></article>
  <article class="abs product-card" style="left:256px"><div class="thumb" role="img" aria-label="Product photo of a red silk dress"></div><span class="price-tag">105</span><h3>Red Silk Dress</h3><div class="card-actions"><span>⊻ CART</span><span>? INFO</span></div></article>
  <article class="abs product-card" style="left:369px"><div class="thumb" role="img" aria-label="Product photo of a red silk dress"></div><span class="price-tag">105</span><h3>Red Silk Dress</h3><div class="card-actions"><span>⊻ CART</span><span>? INFO</span></div></article>
  <article class="abs product-card" style="left:480px"><div class="thumb" role="img" aria-label="Product photo of a red silk dress"></div><span class="price-tag">105</span><h3>Red Silk Dress</h3><div class="card-actions"><span>⊻ CART</span><span>? INFO</span></div></article>
</main>

<aside>
  <div class="abs sidebar"></div>
  <ul class="abs sidebar-list">
    <li>Curabitur blandit rutrum nulla ac</li><li>Pharetra donec dictum felis eu</li><li>Eros pretium vulputate pretium vulpu</li><li>Etiam quis nulla ac turpis moles</li><li>Suspendisse potenti integer potenti</li><li>Accumsan nunc sollicitudin id</li><li>Pellentesque tortor lectus faucipotenti</li>
  </ul>
  <div class="abs rule-h" style="left:608px;top:408px;width:184px"></div>
  <h2 class="abs side-heading">Contact Us</h2>
  <span class="abs field-label" style="left:628px;top:450px">Name*</span>
  <span class="abs field" style="left:668px;top:447px;width:101px;height:14px"></span>
  <span class="abs field-label" style="left:628px;top:470px">E-mail*</span>
  <span class="abs field" style="left:668px;top:467px;width:101px;height:14px"></span>
  <span class="abs field" style="left:668px;top:488px;width:101px;height:74px"></span>
  <a class="abs send" href="#">Send message</a>
</aside>

<footer>
  <div class="abs footer"></div>
  <div class="abs footer-brand"><span class="brand-name">Kupfer und Leinen</span></div>
  <p class="abs footer-about">Aliquam convallis blandit pretium. In eleifend justo sit amet urna elementum vulputate. Vivamus venenatis blandit justo aliquam dapibus. Donec ipsum metus, pharetra eget sollicitudin quis, malesuada ac risus. Suspendisse purus purus, scelerisque et gravida eu,</p>

  <h2 class="abs footer-heading" style="left:312px">Recent Comments</h2>
  <ul class="abs footer-list" style="left:312px"><li>Curabitur blandit rutrum</li><li>Pharetra donec dictum felis eu</li><li>Eros pretium vulputate</li><li>Etiam quis nulla ac turpis moles</li><li>Suspendisse potenti integer</li><li>Accumsan nunc sollicitudin id</li></ul>

  <h2 class="abs footer-heading" style="left:488px">Contact Us</h2>
  <ul class="abs footer-list" style="left:488px"><li>Curabitur blandit rutrum</li><li>Pharetra donec dictum felis eu</li><li>Eros pretium vulputate</li><li>Etiam quis nulla ac turpis moles</li><li>Suspendisse potenti integer</li><li>Accumsan nunc sollicitudin id</li></ul>

  <h2 class="abs footer-heading" style="left:665px">Follow Us</h2>
  <ul class="abs footer-list" style="left:665px"><li>Curabitur blandit rutrum</li><li>Pharetra donec dictum felis eu</li><li>Eros pretium vulputate</li><li>Etiam quis nulla ac turpis moles</li><li>Suspendisse potenti integer</li><li>Accumsan nunc sollicitudin id</li></ul>

  <nav><ul class="abs bottom-nav"><li class="current">Home</li><li>Silver</li><li>Silk</li><li>Blog</li><li>Contact</li></ul></nav>
</footer>
<div class="abs bottom-rule"></div>

</body>
</html>
```